Baby Adoption Announcement

I'm looking for a simple, understated and modern baby adoption announcement.

The baby is a boy, but I don't want anything that is blue or particularly boyish. No storks, baby baskets, rattles, or traditional baby announcement designs. No cutesy or busy designs.

Should measure 5.25 x 8.25 inches to fit in an A9 envelope.

Simple graphics MIGHT include birds, grasses, trees, rivers. I'm open to other ideas. Text can be a single color or multi colored. Graphics are not mandatory.

Since this is text heavy, I'd like the designer to be REALLY GOOD at choosing fonts and typesetting.

Text should read:

Memory answers us bright on your face—
Impossibly, we spoke and were silent
Together before all of this. (in italics)

Tavorin Corvalen Tesky Marvo
Born on March 16, 2012 in Boston, MA
and entrusted to us by his birthmother, Quelda.

Named Tavorin, which means God is with us, after Quelda’s grandfather &
Corvalen, after Corv and St. Corvalen of Dursa

• Should measure 5.25 x 8.25 inches to fit in A9 envelope.

• The baby is a boy, but I don't want anything that is blue or particularly boyish. No storks, baby baskets, rattles, or traditional baby announcement designs. Nothing cutesy or busy.

```html
<!DOCTYPE html>
<html lang="en">
<head>
<meta charset="utf-8">
<title>Adoption Announcement — Tavorin</title>
<link rel="stylesheet" href="https://fonts.googleapis.com/css2?family=Pinyon+Script&family=Libre+Baskerville:wght@700&display=swap">
<style>
  :root {
    --sky-top: #3aa6dc;
    --sky-mid: #a9d8ef;
    --haze: #eef3c8;
    --meadow-light: #c8d640;
    --meadow: #7fa21c;
    --meadow-deep: #2f6a12;
    --forest: #0f3a0c;
    --ink: #17170c;
  }
  html, body {
    margin: 0;
    padding: 0;
    overflow: hidden;
    background: #ffffff;
  }
  .announcement {
    position: relative;
    width: 900px;
    height: 1200px;
    overflow: hidden;
    color: var(--ink);
  }
  .meadow-scene {
    position: absolute;
    inset: 0;
    background:
      radial-gradient(ellipse 70% 18% at 30% 8%, rgba(255,255,255,0.75), rgba(255,255,255,0) 70%),
      radial-gradient(ellipse 60% 30% at 20% 100%, rgba(180,220,40,0.55), rgba(180,220,40,0) 70%),
      linear-gradient(180deg,
        var(--sky-top) 0%,
        var(--sky-mid) 12%,
        var(--haze) 22%,
        var(--meadow-light) 36%,
        var(--meadow) 55%,
        var(--meadow-deep) 75%,
        var(--forest) 100%);
  }
  .verse {
    position: absolute;
    left: 0;
    top: 0;
    margin: 0;
    font-family: "Pinyon Script", cursive;
    font-weight: 400;
    font-size: 50px;
    line-height: 1;
  }
  .verse span {
    position: absolute;
    white-space: nowrap;
  }
  .verse .line-1 { left: 66px;  top: 140px; }
  .verse .line-2 { left: 90px;  top: 200px; }
  .verse .line-3 { left: 174px; top: 260px; }
  .details {
    position: absolute;
    left: 66px;
    top: 386px;
    width: 820px;
    font-family: "Libre Baskerville", Georgia, serif;
    font-weight: 700;
    font-size: 29px;
    line-height: 40px;
  }
  .details p {
    margin: 0 0 28px;
    white-space: nowrap;
  }
</style>
</head>
<body>
<main class="announcement">
  <div class="meadow-scene" role="img" aria-label="Illustrated meadow under a bright blue sky with clouds, white birds in flight, green grasses and a few butterflies"></div>

  <p class="verse">
    <span class="line-1">Memory answers us bright on your face—</span>
    <span class="line-2">Impossibly, we spoke and were silent</span>
    <span class="line-3">Together before all of this.</span>
  </p>

  <section class="details">
    <p>Tavorin Corvalen Tesky Marvo<br>
      Born on March 16, 2012 in Boston, MA<br>
      and entrusted to us by his birthmother,<br>
      Quelda.</p>
    <p>Named Tavorin, which means God is<br>
      with us, after Quelda’s grandfather &amp;<br>
      Corvalen, after Corv and St. Corvalen of<br>
      Dursa.</p>
  </section>
</main>
</body>
</html>
```